Label to go onto food packaging.

We need to create a visually interesting and appealing label to stick onto our take away food packaging. The label should contain information of the food products our cafe sells. The label is to go onto biodegradable food bowls and clam shell packaging.
The information is basically the lines we sell - buddha bowls, super smoothies, vegan burgers and curries. And also the slogan 'nourish and refresh'. We have a logo design that we would like to incorporate onto the label (but not essential)
The design will go onto a rectangle strip label.
The colours of our food outlet are splashes of yellow, blue and grey in a white interior.
We also feature a large garden green wall. You may view images from our instagram page quiet pebble kitchen

Target Market(s)

Young professional, health conscious, plant based eaters. To be used on takeaway packaging.

Industry/Entity Type

Food Production

Font styles to use
Sans Serif

Colors

Designer to choose colors to be used in the design.

Requirements
Must have
• Bold, appealing, informative.
Nice to have
• Logo incorporated, possibly as a watermark?
Should not have
• No floral shapes. If incorporating the logo, use a circle or nothing around it. No pictures/photos of food

```html
<!DOCTYPE html>
<html lang="en">
<head>
<meta charset="utf-8">
<title>Quiet Pebble – Takeaway Label</title>
<link href="https://fonts.googleapis.com/css2?family=Great+Vibes&family=Raleway:wght@300;400;600;700&display=swap" rel="stylesheet">
<style>
  :root{
    --stage:#f4f1e6;
    --paper:#ffffff;
    --ink:#4a4a4a;
    --ink-soft:#8d8d8d;
    --ink-dark:#222222;
    --script-gold:#f2c20c;
    --script-blue:#1a58b8;
    --wash-violet:#b9a2ef;
    --wash-blue:#a9d4f5;
    --sun-orange:#f07c12;
    --sun-yellow:#ffd23a;
    --footer-cream:#f3ecd0;
    --badge-red:#a3202b;
    --badge-pink:#f7c9cf;
  }
  *{box-sizing:border-box;margin:0;padding:0}
  html,body{width:1200px;height:1200px;overflow:hidden;background:var(--stage)}
  body{position:relative;font-family:'Raleway',sans-serif;color:var(--ink)}
  .label{
    position:absolute;left:445px;top:20px;width:378px;height:1415px;
    transform:scale(0.818);transform-origin:top left;
    background:var(--paper);box-shadow:0 2px 8px rgba(0,0,0,.12);overflow:hidden;
  }
  .section{position:absolute;left:0;width:100%;text-align:center}
  .wash{position:absolute;left:0;top:0;width:100%;height:70px;
    background:linear-gradient(100deg,var(--wash-violet),var(--wash-blue) 45%,#fff 60%,var(--wash-violet) 85%,var(--wash-blue));
    opacity:.75;-webkit-mask:linear-gradient(#000 40%,transparent)}
  .script{position:relative;font-family:'Great Vibes',cursive;color:var(--script-gold);font-size:33px;line-height:1;padding-top:10px}
  .bowls{top:0;height:585px}
  .smoothies{top:585px;height:350px}
  .tier{font-size:19px;font-weight:300;color:var(--ink-dark);letter-spacing:.5px;line-height:1;margin-top:2px}
  .item{font-size:11.6px;line-height:14px;padding:0 10px;letter-spacing:-.3px}
  .tags{font-size:11.6px;color:var(--ink-soft);line-height:16px}
  .price-row{display:flex;justify-content:space-between;font-size:11.4px;line-height:17px;padding:0 50px 0 66px;color:var(--ink-soft);letter-spacing:-.3px}
  .blurb{font-size:11.6px;line-height:15px;padding:2px 30px 0;letter-spacing:-.3px;text-align:center;margin-top:2px}
  .blurb .price{float:right}
  .rule{width:92%;margin:4px auto 0;border-top:1px solid #ccc}
  .smoothie-name{font-size:19px;font-weight:300;color:var(--ink-dark);line-height:17px;margin-top:4px}
  .smoothie-desc{font-size:11.4px;line-height:14px;letter-spacing:-.3px}
  .drinks{margin-top:6px}
  .drinks .price-row{padding:0 70px 0 70px;line-height:16.5px;color:var(--ink)}
  .drinks .price-row.solo{justify-content:flex-end}
  .hero{top:935px;height:320px}
  .hero-photo{position:absolute;left:0;top:40px;width:100%;height:240px;
    background:radial-gradient(circle at 45% 55%,#e44a9a 0,#7ab04a 35%,#e6d27a 65%,#f5f0d8 100%)}
  .hero-wave{position:absolute;left:0;bottom:0;width:100%;height:90px}
  .slogan{position:absolute;left:0;top:20px;width:100%;font-family:'Great Vibes',cursive;font-size:46px;color:var(--script-blue);text-align:right;padding-right:12px}
  .brand{position:absolute;left:10px;bottom:10px;font-size:28px;font-weight:600;color:#666;letter-spacing:.3px;text-align:left}
  .legend{top:1255px;height:85px;display:flex;justify-content:space-around;padding:12px 8px 0}
  .legend-item{width:64px;font-size:8px;color:var(--ink-soft);line-height:9px;text-transform:uppercase}
  .legend-item b{color:var(--ink);font-weight:700}
  .legend-icon{width:38px;height:38px;margin:0 auto 6px;border-radius:50%;background:var(--sun-orange);border:3px solid var(--sun-yellow);
    color:#fff;font-size:12px;font-weight:700;display:flex;align-items:center;justify-content:center}
  .footer{top:1340px;height:75px;background:var(--footer-cream);text-align:left}
  .enjoy{position:absolute;left:12px;top:10px;width:95px;height:36px;border:2px solid #111;background:#fff;padding:2px 4px}
  .enjoy small{display:block;font-size:5px;line-height:6px}
  .enjoy strong{display:block;font-size:14px;line-height:14px;text-align:center}
  .enjoy em{display:block;font-size:5px;font-style:normal;text-align:center;font-weight:700}
  .contact{position:absolute;left:125px;top:10px;width:160px;font-size:6.4px;line-height:7.5px;font-weight:700;text-align:center;color:#555}
  .seal{position:absolute;right:12px;top:12px}
  .net{position:absolute;left:10px;top:52px;font-size:11px;color:#666}
</style>
</head>
<body>
<main class="label">

  <section class="section bowls">
    <div class="wash"></div>
    <h2 class="script">Lunch Buddha Bowls</h2>
    <h3 class="tier">GOLD</h3>
    <p class="item">Carrot, lentils, avocado, oasted tomato, mushrooms, cabbage, pickled red onion, labne, spiced nuts, rocket</p>
    <p class="tags">(GF) (VGO)</p>
    <p class="item">Freekeh, broccolini, chickpeas, in kale &amp; almond pesto, pickled purple cabbage, bestroot, chia hazel nut dukkah, kefir</p>
    <p class="tags">(VGO)</p>
    <p class="item">Falafel, coconut yoghurt rajta, quinoa, pickled cabbage, turmeric roasted cauliflower, rocket, roasted pumpkin</p>
    <p class="tags">(VG) (GF)</p>
    <p class="item">Totopos, avocado salsa, capsicum, corn, black beans, tomato, spicy coconut yoghurt dip</p>
    <p class="tags">(VG) (GF)</p>
    <p class="item">Green tea noodles, edamame, bean shoots, sweet potato, spinach, avocado, kimchi, turtle beans, cucumber</p>
    <p class="tags">(VG)</p>
    <p class="item">Asparagus &amp; cucumber salad, turmeric roasted cauliflower, beetroot noodles, roasted pumpkin, quinoa taboulah, avocado, chickpea and tahini</p>
    <p class="tags">(V) (GF) (VGO)</p>
    <h3 class="tier">HOT</h3>
    <p class="item">pumpkin, coconut, chickpea curry with forbidden black rice, kale, natural yoghurt, nuts and seeds</p>
    <p class="tags">(GF)(VGO)</p>
    <p class="item">Sri lankan cauliflower, sweet potato, zucchini, tomato curry with forbidden black rice, kale, coconut yoghurt</p>
    <p class="tags">(GF)(VG)</p>
    <div style="height:10px"></div>
    <div class="price-row"><span>Add pulled chicken, smoked salmon, tofu</span><span>7</span></div>
    <div class="price-row"><span>poached egg/goats chevre</span><span>3/4</span></div>
    <p class="blurb">Nutrient packed bowls of delicious vibrant vegetables-raw and cooked, legumes, grains, seeds, shoots, with the option of adding a protein <span class="price">16.9</span></p>
    <div class="rule"></div>
  </section>

  <section class="section smoothies">
    <div class="wash"></div>
    <h2 class="script">Super Smoothies</h2>
    <h3 class="smoothie-name">BUZZ</h3>
    <p class="smoothie-desc">Banana, date, almond milk, raw cacao, bee pollen</p>
    <h3 class="smoothie-name">MATCHA</h3>
    <p class="smoothie-desc">Mango, spinach, avocado, matcha, coconut milk</p>
    <h3 class="smoothie-name">RUN TO PARADISE</h3>
    <p class="smoothie-desc">Berries, acai, coconut water, banana, passion fruit</p>
    <h3 class="smoothie-name">COOL AS A</h3>
    <p class="smoothie-desc">Cucumber, kale, mango, spurlina, ginger, lemon, coconut water</p>
    <h3 class="smoothie-name">MANGO PASH</h3>
    <p class="smoothie-desc">Mango, passion fruit, coconut water, banana, turmeric</p>
    <h3 class="smoothie-name">DREAM</h3>
    <p class="smoothie-desc">Coconut yoghurt, vanilla, cinnamon, chia seeds, banana, coconut water</p>
    <div class="drinks">
      <div class="price-row solo"><span>9.5</span></div>
      <div class="price-row"><span>Add protein powder</span><span>1.0</span></div>
      <div class="price-row"><span>Kombucha</span><span>6.9</span></div>
      <div class="price-row"><span>Sparkling Apple Cider Vinegar</span><span>6.9</span></div>
      <div class="price-row"><span>Turmeric and Ginger Elixir</span><span>6.9</span></div>
      <div class="price-row"><span>Mineral Water 250ml/750ml</span><span>3.5/6.5</span></div>
    </div>
  </section>

  <section class="section hero">
    <div class="hero-photo" role="img" aria-label="Colourful bowl of fresh vegetables, greens, pickled cabbage and black beans"></div>
    <svg class="hero-wave" viewBox="0 0 378 90" preserveAspectRatio="none" aria-hidden="true">
      <path d="M0 30 C60 5 110 40 170 25 S290 0 378 20 L378 90 L0 90 Z" fill="#ffe27a"/>
      <path d="M0 50 C80 30 150 60 230 45 S330 35 378 45 L378 90 L0 90 Z" fill="#fbd43e"/>
    </svg>
    <p class="slogan">Nourish And Refresh</p>
    <p class="brand">Quiet Pebble</p>
  </section>

  <section class="section legend">
    <div class="legend-item"><div class="legend-icon">VG</div>Vegan</div>
    <div class="legend-item"><div class="legend-icon">V</div>Vegetarian</div>
    <div class="legend-item"><div class="legend-icon">VGO</div>Vegan option<br><b>available</b></div>
    <div class="legend-item"><div class="legend-icon">GF</div>Gluten<br><b>free</b></div>
    <div class="legend-item"><div class="legend-icon">DF</div>Dairy<br><b>free</b></div>
  </section>

  <section class="section footer">
    <div class="enjoy"><small>ENJOY BY:</small><strong>3 JAN</strong><em>434608 09:47</em></div>
    <p class="contact">42 Harbour Lane, Seaview VIC 3999<br>03 9000 0000<br>quietpebblekitchen@example.com<br>Opening Hours:<br>Tuesday to Sunday 6:30am to 4:00pm</p>
    <svg class="seal" width="80" height="34" viewBox="0 0 80 34" aria-hidden="true">
      <rect x="2" y="4" width="76" height="26" rx="13" fill="#fff" stroke="var(--badge-red)" stroke-width="2.5"/>
      <circle cx="16" cy="17" r="12" fill="var(--badge-pink)" stroke="var(--badge-red)" stroke-width="2"/>
    </svg>
    <p class="net">NET WT. 10 OZ (284g)</p>
  </section>

</main>
</body>
</html>
```